Corvale Homes

To produce a business card design for our newly established house building and development company, We have had a logo design done please see attached, our slogan is "crafting the place you call home"
Contact Information for Business Card
Adress on card needs to Read - 58 Elmsworth Lane, Ashcombe, Wrenfordshire WF7 4QT. Director name Dean Vascotti
Requirements
Must have
- Web adress is www.corvale-homes.co.uk
- Email address is info@corvale-homes.co.uk
- phone number 07700 900417

```html
<!DOCTYPE html>
<html lang="en">
<head>
<meta charset="utf-8">
<title>Corvale Homes – Business Card</title>
<link href="https://fonts.googleapis.com/css2?family=Oswald:wght@500&family=Roboto:wght@400;700&display=swap" rel="stylesheet">
<style>
  :root {
    --page-bg: #eeeeee;
    --card-bg: #262626;
    --card-edge: #7cb62f;
    --brand-green: #8cc63f;
    --text-grey: #a6a6a6;
    --text-light: #c8c8c8;
  }
  * { margin: 0; padding: 0; box-sizing: border-box; }
  html, body {
    width: 1200px; height: 1000px; overflow: hidden;
    background: var(--page-bg);
    font-family: "Roboto", Arial, sans-serif;
  }
  .card {
    position: absolute;
    left: 330px;
    width: 540px; height: 340px;
    background: var(--card-bg);
    border-bottom: 4px solid var(--card-edge);
    border-right: 3px solid var(--card-edge);
    box-shadow: 0 10px 24px rgba(0,0,0,0.18);
  }
  .card--front { top: 110px; }
  .card--back { top: 540px; }

  .brand {
    position: absolute; inset: 0;
    display: flex; flex-direction: column; align-items: center; justify-content: center;
  }
  .brand__name {
    display: flex; align-items: center; gap: 14px;
    color: var(--brand-green);
    font-weight: 700; font-size: 44px; letter-spacing: 1px;
    text-transform: uppercase;
  }
  .brand__mark {
    width: 18px; height: 18px; background: var(--brand-green);
  }
  .brand__rule {
    width: 300px; height: 1px; background: var(--text-grey);
    margin: 12px 0 8px;
  }
  .brand__slogan {
    color: var(--brand-green);
    font-size: 9px; letter-spacing: 4px; text-transform: uppercase;
  }

  .person {
    position: absolute; right: 40px; top: 118px; text-align: right;
  }
  .person__name {
    font-family: "Oswald", "Arial Narrow", sans-serif;
    font-weight: 500; font-size: 30px; color: var(--brand-green);
    text-transform: uppercase; line-height: 1;
  }
  .person__role {
    margin-top: 6px;
    font-size: 12px; letter-spacing: 1px; color: var(--text-grey);
    text-transform: uppercase;
  }

  .contact {
    position: absolute; left: 40px; bottom: 38px;
    color: var(--text-light); font-size: 13px; line-height: 1.45;
  }
  .contact__address { margin-bottom: 8px; }
  .contact__list { list-style: none; }
  .contact__item { display: flex; align-items: center; gap: 8px; }
  .contact__icon { width: 11px; height: 11px; flex: none; }
</style>
</head>
<body>

<section class="card card--front" aria-label="Business card front">
  <div class="brand">
    <div class="brand__name"><span class="brand__mark"></span>Corvale Homes</div>
    <div class="brand__rule"></div>
    <div class="brand__slogan">Crafting the place you call home</div>
  </div>
</section>

<section class="card card--back" aria-label="Business card back">
  <div class="person">
    <div class="person__name">Dean Vascotti</div>
    <div class="person__role">Director</div>
  </div>

  <div class="contact">
    <p class="contact__address">58 Elmsworth Lane, Ashcombe<br>Wrenfordshire WF7 4QT</p>
    <ul class="contact__list">
      <li class="contact__item">
        <svg class="contact__icon" viewBox="0 0 12 12" aria-hidden="true"><path d="M2.5 1 L4.5 1 L5.2 3.5 L4 4.4 Q5 6.8 7.6 8 L8.5 6.8 L11 7.5 L11 9.5 Q10 11 8.5 11 Q1 9.5 1 2.8 Q1 1.5 2.5 1 Z" fill="#8cc63f"/></svg>
        07700 900417
      </li>
      <li class="contact__item">
        <svg class="contact__icon" viewBox="0 0 12 12" aria-hidden="true"><rect x="0.5" y="2" width="11" height="8" fill="#8cc63f"/><path d="M0.5 2 L6 6.5 L11.5 2" fill="none" stroke="#262626" stroke-width="1"/></svg>
        info@corvale-homes.co.uk
      </li>
      <li class="contact__item">
        <svg class="contact__icon" viewBox="0 0 12 12" aria-hidden="true"><g fill="none" stroke="#8cc63f" stroke-width="1"><circle cx="6" cy="6" r="5"/><ellipse cx="6" cy="6" rx="2.2" ry="5"/><path d="M1 6 H11 M2 3.5 H10 M2 8.5 H10"/></g></svg>
        www.corvale-homes.co.uk
      </li>
    </ul>
  </div>
</section>

</body>
</html>
```